We need visit card and a letter paper for our website. thx

We have a beauty clinic in Switzerland.
https://wolkenbachtal.ch
We need a visit card.

Requirements
Must have
• see colors on website

```html
<!DOCTYPE html>
<html lang="de">
<head>
<meta charset="utf-8">
<title>Wolkenbachtal – Visitenkarte</title>
<link href="https://fonts.googleapis.com/css2?family=Roboto:wght@300;400;500&display=swap" rel="stylesheet">
<style>
  :root {
    --backdrop: #ecebeb;
    --card: #2f2f2f;
    --ink: #ffffff;
    --ink-soft: #d6d6d6;
    --rule: #8a8a8a;
  }
  * { margin: 0; padding: 0; box-sizing: border-box; }
  html, body { width: 1200px; height: 801px; overflow: hidden; }
  body {
    background: var(--backdrop);
    font-family: "Roboto", Arial, sans-serif;
    color: var(--ink);
    position: relative;
  }
  .card {
    position: absolute;
    top: 232px;
    width: 520px;
    height: 336px;
    background: var(--card);
  }
  .card--back { left: 50px; }
  .card--front { left: 630px; }

  .brand {
    position: absolute;
    display: flex;
    align-items: center;
    gap: 12px;
  }
  .brand__mark {
    width: 12px; height: 12px;
    border: 1px solid var(--ink);
  }
  .brand__name {
    font-weight: 300;
    color: var(--ink);
    letter-spacing: 0.5px;
  }
  .card--back .brand { left: 48px; top: 152px; }
  .card--back .brand__name { font-size: 26px; }
  .card--front .brand { left: 90px; top: 230px; }
  .card--front .brand__name { font-size: 38px; }

  .divider {
    position: absolute;
    left: 268px; top: 40px;
    width: 1px; height: 256px;
    background: var(--rule);
  }
  .contact {
    position: absolute;
    left: 294px; top: 62px;
    font-size: 13px;
    line-height: 1.45;
    color: var(--ink-soft);
    font-weight: 300;
  }
  .contact__name { font-size: 16px; font-weight: 500; color: var(--ink); }
  .contact__role { margin-bottom: 16px; }
  .contact__address { margin-bottom: 16px; }
  .contact__line { display: flex; align-items: center; gap: 8px; }
  .contact__line svg { width: 11px; height: 11px; flex: none; }
</style>
</head>
<body>
  <section class="card card--back">
    <div class="brand">
      <span class="brand__mark"></span>
      <span class="brand__name">Wolkenbachtal</span>
    </div>
    <div class="divider"></div>
    <div class="contact">
      <p class="contact__name">Dr. Lena Marbach</p>
      <p class="contact__role">FÄ für Plastische Chirurgie</p>
      <p class="contact__address">Talweg 24<br>7550 Scuol, Schweiz</p>
      <p class="contact__line">
        <svg viewBox="0 0 12 12"><path d="M2.5 1h2l1 3-1.3 1a6 6 0 0 0 2.8 2.8L8 6.5l3 1v2A1.5 1.5 0 0 1 9.5 11 8.5 8.5 0 0 1 1 2.5 1.5 1.5 0 0 1 2.5 1z" fill="#d6d6d6"/></svg>
        +41 (0) 800 24 60 60
      </p>
      <p class="contact__line">
        <svg viewBox="0 0 12 12"><rect x="1" y="2.5" width="10" height="7" fill="none" stroke="#d6d6d6"/><path d="M1 2.5l5 4 5-4" fill="none" stroke="#d6d6d6"/></svg>
        hallo@wolkenbachtal.ch
      </p>
      <p class="contact__line">
        <svg viewBox="0 0 12 12"><circle cx="6" cy="6" r="5" fill="none" stroke="#d6d6d6"/><path d="M1 6h10M6 1c-2.5 3-2.5 7 0 10M6 1c2.5 3 2.5 7 0 10" fill="none" stroke="#d6d6d6" stroke-width=".8"/></svg>
        www.wolkenbachtal.ch
      </p>
    </div>
  </section>

  <section class="card card--front">
    <div class="brand">
      <span class="brand__mark"></span>
      <span class="brand__name">Wolkenbachtal</span>
    </div>
  </section>
</body>
</html>
```